Process Roadmap for Interior Design Firm

We are looking to ramp up the design appeal of our current process roadmap to be very visually interesting, while staying informative and descriptive about our process.

Target Market(s)

In-house Clients

Industry/Entity Type

Interior Design Firm focused on sustainable and holistic design.

Other font styles liked:
• raleway

Requirements
Must have
• 1.) it would be nice if the graphic provided a more clear indication of the “journey” from one step to the next, so that there was a clear sense of the progression (such that we are directing the viewer) 2.). We would want it to fit on an 8.5”x11” page (the page could be horizontal when we have the Calm Compass formatted out with the testimonials) (in addition to the testimonials, we may also want to have the detailed descriptions of each step of the process presented below the graphic, so that the graphic is cleaner) 3.) ideally the graphic is clear and simple enough to also be used on our Bi-Weekly Client Updates, which will be typed updates for clients re their project budgets, schedule and scope. The Calm Compass graphic (without all the testimonials) would be at the end of the update, and would fit on the page horizontally at the bottom, perhaps in a space which is 7.5”w x 4”h or so.
Should not have
• bold or bright colors. Natural neutrals are preferred, such as the ones featured on the provided graphic.

```html
<!DOCTYPE html>
<html lang="en">
<head>
<meta charset="utf-8">
<title>LVH Calm Compass – Process Roadmap</title>
<link href="https://fonts.googleapis.com/css2?family=Oswald:wght@400;500;600&family=Roboto+Condensed:wght@400&display=swap" rel="stylesheet">
<style>
  :root {
    --sky-top: #a9d8f0;
    --sky-bottom: #e3f3fb;
    --room-dark: #1d4f78;
    --room-mid: #3f86b8;
    --room-light: #8cc2e2;
    --accent: #1a8fd6;
    --accent-soft: #5fb6e6;
    --accent-deep: #2a78b4;
    --ink: #1f3446;
    --white: #ffffff;
    --card: rgba(255, 255, 255, 0.8);
  }
  * { box-sizing: border-box; margin: 0; padding: 0; }
  html, body { width: 1200px; height: 848px; overflow: hidden; }
  body { font-family: "Roboto Condensed", "Arial Narrow", sans-serif; color: var(--ink); }
  .roadmap {
    position: relative;
    width: 1200px;
    height: 848px;
    overflow: hidden;
    background: linear-gradient(180deg, var(--sky-top) 0%, var(--sky-bottom) 60%);
  }
  .backdrop { position: absolute; inset: 0; }

  .step-icon,
  .step-title,
  .step-text { position: absolute; }
  .step-icon {
    left: calc(var(--x) - 25px);
    top: var(--icon-top);
    width: 54px;
    height: 54px;
  }
  .step-title {
    left: calc(var(--x) - 90px);
    top: var(--title-top);
    width: 180px;
    text-align: center;
    font-family: "Oswald", "Arial Narrow", sans-serif;
    font-weight: 400;
    font-size: 30px;
    line-height: 1;
    color: var(--accent);
  }
  .step-text {
    left: calc(var(--x) - 76px);
    top: var(--text-top);
    width: 152px;
    text-align: center;
    font-size: 12.5px;
    line-height: 15.5px;
  }

  .testimonial {
    position: absolute;
    top: 694px;
    width: 150px;
    height: 126px;
    padding: 10px 10px 8px 12px;
    background: var(--card);
    font-size: 13px;
    line-height: 1.2;
  }
  .testimonial .quote-badge {
    position: absolute;
    left: -12px;
    top: -24px;
    width: 36px;
    height: 30px;
  }
  .testimonial cite { font-style: normal; display: block; }
</style>
</head>
<body>
<main class="roadmap">
  <svg class="backdrop" width="1200" height="848" viewBox="0 0 1200 848">
    <defs>
      <linearGradient id="roomTone" x1="0" y1="0" x2="0" y2="1">
        <stop offset="0" stop-color="var(--room-light)"/>
        <stop offset="0.45" stop-color="var(--room-mid)"/>
        <stop offset="1" stop-color="var(--room-dark)"/>
      </linearGradient>
      <filter id="titleShadow" x="-10%" y="-30%" width="120%" height="160%">
        <feDropShadow dx="2" dy="3" stdDeviation="2" flood-color="#0f3a5c" flood-opacity="0.7"/>
      </filter>
      <path id="titleCurve" d="M 230 490 Q 600 370 970 490"/>
    </defs>

    <g class="light-rays" fill="var(--white)" opacity="0.35">
      <polygon points="1080,330 1200,120 1200,170"/>
      <polygon points="1080,330 1200,230 1200,270"/>
      <polygon points="1080,330 1160,0 1200,0"/>
      <polygon points="1080,330 1040,0 1080,0"/>
      <polygon points="1080,330 1200,330 1200,360"/>
    </g>

    <path class="interior-photo" role="img" aria-label="Photo of a bright living room with large windows, armchair, fireplace and dining table"
          d="M -10 500 C 250 300, 950 300, 1210 500 L 1210 860 L -10 860 Z" fill="url(#roomTone)"/>

    <path class="journey-arc" d="M -10 500 C 250 300, 950 300, 1210 500"
          fill="none" stroke="var(--white)" stroke-width="9"/>

    <g class="connectors" stroke="var(--white)" stroke-width="1.5">
      <line x1="112" y1="348" x2="112" y2="412"/>
      <line x1="272" y1="318" x2="272" y2="363"/>
      <line x1="928" y1="330" x2="928" y2="363"/>
    </g>

    <g class="milestones" font-family="Oswald, sans-serif" font-weight="600" font-size="27" fill="var(--accent)" text-anchor="middle">
      <circle cx="112" cy="432" r="21" fill="var(--white)"/><text x="112" y="442">1</text>
      <circle cx="272" cy="383" r="21" fill="var(--white)"/><text x="272" y="393">2</text>
      <circle cx="429" cy="359" r="21" fill="var(--white)"/><text x="429" y="369">3</text>
      <circle cx="600" cy="350" r="21" fill="var(--white)"/><text x="600" y="360">4</text>
      <circle cx="771" cy="359" r="21" fill="var(--white)"/><text x="771" y="369">5</text>
      <circle cx="928" cy="383" r="21" fill="var(--white)"/><text x="928" y="393">6</text>
      <circle cx="1088" cy="432" r="21" fill="var(--white)"/><text x="1088" y="442">7</text>
    </g>

    <text class="roadmap-title" font-family="Oswald, sans-serif" font-weight="500" font-size="60"
          fill="var(--white)" filter="url(#titleShadow)" letter-spacing="1">
      <textPath href="#titleCurve" startOffset="50%" text-anchor="middle">LVH CALM COMPASS</textPath>
    </text>
  </svg>

  <section class="step" style="--x:112px; --icon-top:116px; --title-top:208px; --text-top:262px;">
    <svg class="step-icon" viewBox="0 0 54 54" aria-hidden="true">
      <polygon points="6,10 14,2 52,2 44,10" fill="var(--accent-soft)"/>
      <polygon points="44,10 52,2 52,40 44,48" fill="var(--accent-deep)"/>
      <rect x="6" y="10" width="38" height="38" fill="var(--accent)"/>
      <path d="M13 30 L25 19 L37 30 M16 28 V40 H34 V28" fill="none" stroke="var(--white)" stroke-width="3"/>
      <rect x="22" y="32" width="6" height="8" fill="var(--white)"/>
    </svg>
    <h2 class="step-title">Listening</h2>
    <p class="step-text">Listening to our clients, their land, and their home. Identify their needs, challenges, wishes, and dreams.</p>
  </section>

  <section class="step" style="--x:272px; --icon-top:66px; --title-top:160px; --text-top:210px;">
    <svg class="step-icon" viewBox="0 0 54 54" aria-hidden="true">
      <polygon points="6,10 14,2 52,2 44,10" fill="var(--accent-soft)"/>
      <polygon points="44,10 52,2 52,40 44,48" fill="var(--accent-deep)"/>
      <rect x="6" y="10" width="38" height="38" fill="var(--accent)"/>
      <circle cx="23" cy="27" r="9" fill="none" stroke="var(--white)" stroke-width="3"/>
      <line x1="29.5" y1="33.5" x2="38" y2="42" stroke="var(--white)" stroke-width="4"/>
    </svg>
    <h2 class="step-title">Visioning</h2>
    <p class="step-text">Faciliting a guided visioning process to clarify the deepest intention, true purpose, and highest potential for their home and their future within it.</p>
  </section>

  <section class="step" style="--x:433px; --icon-top:30px; --title-top:128px; --text-top:178px;">
    <svg class="step-icon" viewBox="0 0 54 54" aria-hidden="true">
      <polygon points="6,10 14,2 52,2 44,10" fill="var(--accent-soft)"/>
      <polygon points="44,10 52,2 52,40 44,48" fill="var(--accent-deep)"/>
      <rect x="6" y="10" width="38" height="38" fill="var(--accent)"/>
      <path d="M16 41 L18 33 L32 17 L37 22 L23 37 Z" fill="var(--white)"/>
    </svg>
    <h2 class="step-title">Planning</h2>
    <p class="step-text">Turning our client's vision into a clearly defined scope, budget, and timeline. Mapping out the steps for making their dream a reality.<br>Setting a meeting schudule from start to finish.</p>
  </section>

  <section class="step" style="--x:600px; --icon-top:18px; --title-top:128px; --text-top:180px;">
    <svg class="step-icon" viewBox="0 0 54 54" aria-hidden="true">
      <polygon points="6,10 14,2 52,2 44,10" fill="var(--accent-soft)"/>
      <polygon points="44,10 52,2 52,40 44,48" fill="var(--accent-deep)"/>
      <rect x="6" y="10" width="38" height="38" fill="var(--accent)"/>
      <circle cx="25" cy="26" r="7" fill="none" stroke="var(--white)" stroke-width="2.5"/>
      <rect x="22" y="34" width="6" height="5" fill="var(--white)"/>
      <g stroke="var(--white)" stroke-width="2">
        <line x1="25" y1="13" x2="25" y2="16"/><line x1="13" y1="26" x2="16" y2="26"/>
        <line x1="34" y1="26" x2="37" y2="26"/><line x1="16" y1="17" x2="18" y2="19"/>
        <line x1="34" y1="17" x2="32" y2="19"/>
      </g>
    </svg>
    <h2 class="step-title">Designing</h2>
    <p class="step-text">Following the schudule through the design phases from initial design concepts, technical drawings and details, and the selection of all finishes, fixtures, and furnishings.</p>
  </section>

  <section class="step" style="--x:762px; --icon-top:28px; --title-top:128px; --text-top:180px;">
    <svg class="step-icon" viewBox="0 0 54 54" aria-hidden="true">
      <polygon points="6,10 14,2 52,2 44,10" fill="var(--accent-soft)"/>
      <polygon points="44,10 52,2 52,40 44,48" fill="var(--accent-deep)"/>
      <rect x="6" y="10" width="38" height="38" fill="var(--accent)"/>
      <circle cx="25" cy="29" r="10" fill="none" stroke="var(--white)" stroke-width="3" stroke-dasharray="4 2"/>
      <path d="M20 29 L24 33 L31 25" fill="none" stroke="var(--white)" stroke-width="3"/>
    </svg>
    <h2 class="step-title">Managing</h2>
    <p class="step-text">Coordinating with clients, builders, architects, and vendors to ensure that the design is executed with excellence, and the construction and furnishings are on-time and on-budget</p>
  </section>

  <section class="step" style="--x:924px; --icon-top:64px; --title-top:162px; --text-top:210px;">
    <svg class="step-icon" viewBox="0 0 54 54" aria-hidden="true">
      <polygon points="6,10 14,2 52,2 44,10" fill="var(--accent-soft)"/>
      <polygon points="44,10 52,2 52,40 44,48" fill="var(--accent-deep)"/>
      <rect x="6" y="10" width="38" height="38" fill="var(--accent)"/>
      <path d="M14 20 L24 16 L30 22 L26 26 Z" fill="var(--white)"/>
      <line x1="25" y1="24" x2="37" y2="40" stroke="var(--white)" stroke-width="4"/>
    </svg>
    <h2 class="step-title">Installing</h2>
    <p class="step-text">Overseeing the inspection, installation, and arrangement of all furnishings, lighting, artwork, and decorative items.<br>Taling care of every last detail.</p>
  </section>

  <section class="step" style="--x:1086px; --icon-top:114px; --title-top:210px; --text-top:262px;">
    <svg class="step-icon" viewBox="0 0 54 54" aria-hidden="true">
      <polygon points="6,10 14,2 52,2 44,10" fill="var(--accent-soft)"/>
      <polygon points="44,10 52,2 52,40 44,48" fill="var(--accent-deep)"/>
      <rect x="6" y="10" width="38" height="38" fill="var(--accent)"/>
      <path d="M14 28 L22 36 L37 19" fill="none" stroke="var(--white)" stroke-width="5"/>
    </svg>
    <h2 class="step-title">Completing</h2>
    <p class="step-text">Fixing any issues or defects<br>Follow up in all remaining items.<br>Completing the final finishing touches to our client's full and total satisfaction.</p>
  </section>

  <aside class="testimonial" style="left:57px;">
    <svg class="quote-badge" viewBox="0 0 36 30" aria-hidden="true">
      <path d="M2 2 H34 V22 H12 L6 28 V22 H2 Z" fill="var(--accent)"/>
      <circle cx="11" cy="12" r="2.6" fill="var(--white)"/><circle cx="18" cy="12" r="2.6" fill="var(--white)"/><circle cx="25" cy="12" r="2.6" fill="var(--white)"/>
    </svg>
    <p>"The result was better than expected. The design, construction, and completion of the highest quality"</p>
    <cite>(Helen Carter, NY)</cite>
  </aside>

  <aside class="testimonial" style="left:257px;">
    <svg class="quote-badge" viewBox="0 0 36 30" aria-hidden="true">
      <path d="M2 2 H34 V22 H12 L6 28 V22 H2 Z" fill="var(--accent)"/>
      <circle cx="11" cy="12" r="2.6" fill="var(--white)"/><circle cx="18" cy="12" r="2.6" fill="var(--white)"/><circle cx="25" cy="12" r="2.6" fill="var(--white)"/>
    </svg>
    <p>"The result was better than expected. The design, construction, and completion of the highest quality"</p>
    <cite>(Helen Carter, NY)</cite>
  </aside>

  <aside class="testimonial" style="left:1022px;">
    <svg class="quote-badge" viewBox="0 0 36 30" aria-hidden="true">
      <path d="M2 2 H34 V22 H12 L6 28 V22 H2 Z" fill="var(--accent)"/>
      <circle cx="11" cy="12" r="2.6" fill="var(--white)"/><circle cx="18" cy="12" r="2.6" fill="var(--white)"/><circle cx="25" cy="12" r="2.6" fill="var(--white)"/>
    </svg>
    <p>"The result was better than expected. The design, construction, and completion of the highest quality"</p>
    <cite>(Helen Carter, NY)</cite>
  </aside>
</main>
</body>
</html>
```